Small dedicated blog website

I have recently had a logo designed for my growing personal hobby, I document my adventures around the world in video form (www.vidstream-example.com/marlowventures.com) I am now trying to create a small blog website with easy access to my other social networks to start to create a home base for all the videos and content I create, I would like a simple website with a focus on blog posts and access to my other social networks, instagram (marlowventures), facebook (marlowventures), snapchat (glenmarlow)

My current website can be viewed at www.marlowventures-example.com

Please contact me for any further information to help this project

Many thanks!

I do not expect a fully coded website, simply designs and graphics

Industry/Entity Type

Social

Font styles to use
Sans Serif

Requirements
Must have
• area for tumblr blog placement, access to social media links

```html
<!DOCTYPE html>
<html lang="en">
<head>
<meta charset="utf-8">
<title>Marlow Ventures</title>
<link href="https://fonts.googleapis.com/css2?family=Roboto+Condensed:wght@400;700&family=Roboto:ital,wght@0,400;1,400&display=swap" rel="stylesheet">
<style>
  :root {
    --ink: #222222;
    --muted: #666666;
    --panel-dark: #232323;
    --panel-black: #000000;
    --tab-dark: #3d3d3d;
    --logo-bg: #d2d2d4;
    --arrow-bg: #8a8a8a;
    --arrow-dark: #4a4a4a;
    --white: #ffffff;
    --light-text: #d8d8d8;
    --social: #6f7780;
  }
  * { box-sizing: border-box; margin: 0; padding: 0; }
  html, body { width: 1098px; height: 1200px; overflow: hidden; background: var(--white); }
  body { font-family: "Roboto", Arial, sans-serif; color: var(--ink); }
  .cond { font-family: "Roboto Condensed", "Arial Narrow", sans-serif; }

  .site { position: absolute; left: 156px; top: 0; width: 775px; height: 1200px; }

  /* header */
  .site-header { position: absolute; top: 0; left: 0; width: 775px; height: 87px; display: flex; }
  .brand { width: 181px; height: 87px; background: var(--logo-bg); display: flex; align-items: flex-end; justify-content: center; padding-bottom: 9px; gap: 6px; }
  .brand-dot { width: 8px; height: 8px; background: var(--ink); margin-bottom: 3px; }
  .brand-name { font-family: "Roboto Condensed", sans-serif; font-weight: 700; font-size: 12px; color: var(--ink); letter-spacing: 0.2px; }
  .main-nav { display: flex; height: 87px; }
  .main-nav a { font-family: "Roboto Condensed", sans-serif; font-size: 13px; color: #333; text-decoration: none; display: flex; align-items: center; justify-content: center; height: 87px; }
  .main-nav a.active { background: var(--tab-dark); color: var(--white); width: 119px; }
  .main-nav .n-about { width: 116px; } .main-nav .n-videos { width: 118px; }
  .main-nav .n-blog { width: 95px; } .main-nav .n-contact { width: 130px; }

  /* hero */
  .hero { position: absolute; top: 87px; left: 0; width: 775px; height: 353px;
    background: linear-gradient(180deg, #e7a24f 0%, #e08a3d 22%, #9a6a5a 45%, #405572 62%, #2a3a56 80%, #1b2436 100%); }
  .hero-title { position: absolute; left: 37px; top: 230px; font-family: "Roboto Condensed", sans-serif; font-size: 45px; color: var(--white); letter-spacing: -0.5px; line-height: 1; }
  .hero-tagline { position: absolute; left: 39px; top: 284px; width: 430px; font-family: "Roboto Condensed", sans-serif; font-size: 12px; line-height: 22px; color: var(--white); text-transform: uppercase; }
  .hero-arrows { position: absolute; right: 19px; top: 305px; display: flex; gap: 1px; }
  .hero-arrows span { width: 27px; height: 27px; background: rgba(120,120,130,0.75); display: flex; align-items: center; justify-content: center; }

  /* news */
  .news { position: absolute; top: 440px; left: 0; width: 775px; height: 98px; background: var(--panel-dark); }
  .news-label { position: absolute; left: 33px; top: 23px; font-family: "Roboto Condensed", sans-serif; font-size: 16px; color: var(--white); }
  .news-arrows { position: absolute; left: 90px; top: 48px; display: flex; gap: 1px; }
  .news-arrows span { width: 15px; height: 15px; background: var(--arrow-bg); display: flex; align-items: center; justify-content: center; }
  .news-divider { position: absolute; left: 144px; top: 22px; width: 1px; height: 56px; background: #555; }
  .news-body { position: absolute; left: 166px; top: 21px; width: 590px; font-size: 9px; line-height: 19px; color: var(--light-text); }
  .news-date { font-style: italic; color: var(--white); }

  /* about */
  .section-title { font-family: "Roboto Condensed", sans-serif; font-size: 21px; color: var(--ink); font-weight: 400; }
  .about-title { position: absolute; left: 0; top: 559px; }
  .portrait-frame { position: absolute; left: 0; top: 602px; width: 158px; height: 188px; background: var(--panel-dark); padding: 6px; }
  .portrait { width: 100%; height: 100%; background: linear-gradient(160deg, #c9a68a 0%, #b88c70 50%, #6e5a52 100%); }
  .about-lead { position: absolute; left: 180px; top: 605px; width: 350px; font-family: "Roboto Condensed", sans-serif; font-size: 12px; line-height: 19px; color: var(--ink); }
  .about-body { position: absolute; left: 181px; top: 647px; width: 330px; font-size: 9px; line-height: 19.4px; color: var(--muted); }
  .about-body p + p { margin-top: 19px; }

  /* videos */
  .videos-title { position: absolute; left: 557px; top: 560px; }
  .video-arrows { position: absolute; right: 0; top: 565px; display: flex; gap: 1px; }
  .video-arrows span { width: 15px; height: 15px; background: #a8a8a8; display: flex; align-items: center; justify-content: center; }
  .video { position: absolute; left: 557px; top: 600px; width: 218px; height: 176px; background: #111; }
  .video-frame { width: 218px; height: 158px; background: linear-gradient(135deg, #8a8e94 0%, #b7a497 45%, #6f7b8c 100%); position: relative; }
  .video-play { position: absolute; left: 89px; top: 58px; }
  .video-bar { height: 18px; display: flex; align-items: center; gap: 6px; padding: 0 6px; font-size: 7px; color: #ddd; background: linear-gradient(#2b2b2b, #111); }
  .video-track { width: 78px; height: 4px; background: #555; position: relative; margin-left: 10px; }
  .video-track::before { content: ""; position: absolute; left: 0; top: 0; width: 10px; height: 4px; background: #c22; }
  .video-track::after { content: ""; position: absolute; left: 8px; top: -2px; width: 8px; height: 8px; border-radius: 50%; background: #ddd; }

  /* recent posts */
  .recent { position: absolute; left: 0; top: 818px; width: 775px; height: 260px; background: var(--panel-black); }
  .recent-title { position: absolute; left: 28px; top: 23px; font-family: "Roboto Condensed", sans-serif; font-size: 16px; color: var(--white); }
  .recent-arrows { position: absolute; right: 24px; top: 24px; display: flex; gap: 1px; }
  .recent-arrows span { width: 15px; height: 15px; background: var(--arrow-dark); display: flex; align-items: center; justify-content: center; }
  .posts { position: absolute; left: 25px; top: 60px; display: flex; gap: 22px; }
  .post { width: 165px; }
  .post-thumb { width: 165px; height: 108px; }
  .thumb-plane { background: linear-gradient(180deg, #c99a5a 0%, #8a6a44 60%, #4a3a2a 100%); }
  .thumb-bag { background: linear-gradient(135deg, #6e5f6a 0%, #4b4148 60%, #2e2a2c 100%); }
  .thumb-room { background: linear-gradient(180deg, #d8d6d2 0%, #b2aea8 60%, #4a4644 100%); }
  .thumb-card { background: linear-gradient(160deg, #f1ede2 0%, #e7e2d4 50%, #2d63b0 100%); }
  .post-title { margin-top: 19px; font-family: "Roboto Condensed", sans-serif; font-weight: 700; font-size: 9px; color: var(--white); letter-spacing: -0.2px; }
  .post-excerpt { margin-top: 7px; font-size: 9px; font-style: italic; line-height: 17px; color: var(--light-text); }

  /* footer */
  .site-footer { position: absolute; left: 0; top: 1092px; width: 775px; height: 60px; border-top: 2px solid #e2e2e2; background: linear-gradient(#f3f3f3, #ffffff 70%); }
  .footer-nav { position: absolute; left: 22px; top: 16px; display: flex; gap: 27px; }
  .footer-nav a { font-family: "Roboto Condensed", sans-serif; font-size: 10px; color: #333; text-decoration: none; }
  .copyright { position: absolute; left: 22px; top: 42px; font-family: "Roboto Condensed", sans-serif; font-size: 9.5px; color: #333; }
  .follow { position: absolute; right: 19px; top: 26px; display: flex; align-items: center; gap: 5px; }
  .follow-label { font-family: "Roboto Condensed", sans-serif; font-size: 9.5px; color: #333; margin-right: 1px; }
  .social { width: 25px; height: 25px; border-radius: 50%; background: var(--social); display: block; }
</style>
</head>
<body>
<div class="site">
  <header class="site-header">
    <div class="brand"><span class="brand-dot"></span><span class="brand-name">MARLOWVENTURES.COM</span></div>
    <nav class="main-nav">
      <a class="active" href="#">HOME</a>
      <a class="n-about" href="#">ABOUT US</a>
      <a class="n-videos" href="#">VIDEOS</a>
      <a class="n-blog" href="#">BLOG</a>
      <a class="n-contact" href="#">CONTACT US</a>
    </nav>
  </header>

  <section class="hero" role="img" aria-label="Private jet parked on a wet runway at sunset">
    <h1 class="hero-title">MARLOW VENTURES</h1>
    <p class="hero-tagline">I'm a tri-citizen of our beautiful planet and this is my diary of my various adventures recent relocation to Finland</p>
    <div class="hero-arrows">
      <span><svg width="10" height="14" viewBox="0 0 10 14"><path d="M8 1 2 7l6 6" fill="none" stroke="#fff" stroke-width="1.3"/></svg></span>
      <span><svg width="10" height="14" viewBox="0 0 10 14"><path d="M2 1l6 6-6 6" fill="none" stroke="#fff" stroke-width="1.3"/></svg></span>
    </div>
  </section>

  <section class="news">
    <h2 class="news-label">LATEST NEWS</h2>
    <div class="news-arrows">
      <span><svg width="6" height="8" viewBox="0 0 6 8"><path d="M5 1 1 4l4 3" fill="none" stroke="#fff"/></svg></span>
      <span><svg width="6" height="8" viewBox="0 0 6 8"><path d="M1 1l4 3-4 3" fill="none" stroke="#fff"/></svg></span>
    </div>
    <div class="news-divider"></div>
    <div class="news-body">
      <p>The end of yet another typical Tuesday working behind a reception desk, today I organised my health and travel insurance! I am a British citizen but because I'm not a British am a British citizen but because I'm not a British</p>
      <p class="news-date">Posted on 27 Mar 2014</p>
    </div>
  </section>

  <h2 class="section-title about-title">About Marlow Ventures</h2>
  <div class="portrait-frame"><div class="portrait" role="img" aria-label="Portrait of the blogger wearing sunglasses"></div></div>
  <p class="about-lead">i'm a tri-citizen of our beautiful planet and this is my diary of my various adventures recent relocation to Finland</p>
  <div class="about-body">
    <p>It is a long established fact that a reader will be distracted by the readable content of a page when looking at its layout. The point of using Lorem Ipsum is that it has a more-or-less normal distribution of letters, as opposed to using 'Content here, content here', making it look like readable English.</p>
    <p>Many desktop publishing packages and web page editors now use Lorem Ipsum as their default model text, and a search for will uncover...</p>
  </div>

  <h2 class="section-title videos-title">Our Videos</h2>
  <div class="video-arrows">
    <span><svg width="6" height="8" viewBox="0 0 6 8"><path d="M5 1 1 4l4 3" fill="none" stroke="#fff"/></svg></span>
    <span><svg width="6" height="8" viewBox="0 0 6 8"><path d="M1 1l4 3-4 3" fill="none" stroke="#fff"/></svg></span>
  </div>
  <div class="video">
    <div class="video-frame" role="img" aria-label="Video still of the blogger talking to camera">
      <svg class="video-play" width="38" height="38" viewBox="0 0 38 38"><circle cx="19" cy="19" r="18" fill="rgba(90,90,90,0.6)" stroke="rgba(255,255,255,0.5)"/><path d="M15 11v16l13-8z" fill="rgba(255,255,255,0.7)"/></svg>
    </div>
    <div class="video-bar">
      <svg width="8" height="8" viewBox="0 0 8 8"><rect x="1" y="0" width="2" height="8" fill="#ccc"/><rect x="5" y="0" width="2" height="8" fill="#ccc"/></svg>
      <svg width="14" height="8" viewBox="0 0 14 8"><path d="M0 3h2l3-3v8L2 5H0z" fill="#888"/><path d="M7 5h1v3H7zm2-2h1v5H9zm2-2h1v7h-1z" fill="#666"/></svg>
      <span>0:04 / 0:30</span>
      <span class="video-track"></span>
    </div>
  </div>

  <section class="recent">
    <h2 class="recent-title">RECENT POSTS</h2>
    <div class="recent-arrows">
      <span><svg width="6" height="8" viewBox="0 0 6 8"><path d="M5 1 1 4l4 3" fill="none" stroke="#fff"/></svg></span>
      <span><svg width="6" height="8" viewBox="0 0 6 8"><path d="M1 1l4 3-4 3" fill="none" stroke="#fff"/></svg></span>
    </div>
    <div class="posts">
      <article class="post"><div class="post-thumb thumb-plane" role="img" aria-label="Airliner landing under a golden sky"></div><h3 class="post-title">THE END OF YET ANOTHER TYPICAL</h3><p class="post-excerpt">The end of yet another typical Tuesday working behind a reception...</p></article>
      <article class="post"><div class="post-thumb thumb-bag" role="img" aria-label="Packed travel bag with rolled clothes"></div><h3 class="post-title">THE END OF YET ANOTHER TYPICAL</h3><p class="post-excerpt">The end of yet another typical Tuesday working behind a reception...</p></article>
      <article class="post"><div class="post-thumb thumb-room" role="img" aria-label="Bright living room with white sofa"></div><h3 class="post-title">THE END OF YET ANOTHER TYPICAL</h3><p class="post-excerpt">The end of yet another typical Tuesday working behind a reception...</p></article>
      <article class="post"><div class="post-thumb thumb-card" role="img" aria-label="Health and travel insurance card"></div><h3 class="post-title">THE END OF YET ANOTHER TYPICAL</h3><p class="post-excerpt">The end of yet another typical Tuesday working behind a reception...</p></article>
    </div>
  </section>

  <footer class="site-footer">
    <nav class="footer-nav">
      <a href="#">HOME</a><a href="#">ABOUT US</a><a href="#">VIDEOS</a><a href="#">BLOG</a><a href="#">CONTACT US</a>
    </nav>
    <p class="copyright">© COPYRIGHT 2014. MARLOW VENTURES. ALL RIGHTS RESERVED.</p>
    <div class="follow">
      <span class="follow-label">FOLLOW US :</span>
      <a class="social" href="#" aria-label="Social network one"></a>
      <a class="social" href="#" aria-label="Social network two"></a>
      <a class="social" href="#" aria-label="Video channel"></a>
    </div>
  </footer>
</div>
</body>
</html>
```